Pinecrest Premier Motors *

Professional business cards for our auto wholesale dealership.

Target Market(s)

New and used cars sales managers and middle class to higher end private party buyers.

Industry/Entity Type

Automotive

Contact Information for Business Card

Pinecrest Premier Motors
Marcus T Holloran
Owner
(555) 014-3862
pineprem@mailvista.example
Dealer Lic # 48265

Logo Text

Pinecrest Premier Motors, Pine Prem Motors, PPM, etc

Font styles to use
Serif
Sans Serif

Colors

Designer to choose colors to be used in the design.

Requirements
Must have
• A professional, but not pretentious, look
Nice to have
• It might be nice to see "PPM" in a shape form i.e. circle, triangle, etc in the corner or background somehwere
Should not have
• bright "girly" colors

```html
<!DOCTYPE html>
<html lang="en">
<head>
<meta charset="utf-8">
<title>Pinecrest Premier Motors – Business Card</title>
<link rel="stylesheet" href="https://fonts.googleapis.com/css2?family=Ubuntu:wght@400;500;700&display=swap">
<style>
  :root {
    --backdrop: #3a3d42;
    --card-top: #2b2f36;
    --card-bottom: #1d2026;
    --lime: #a6c812;
    --lime-deep: #86a90a;
    --white: #ffffff;
    --ink: #1f232a;
  }
  * { margin: 0; padding: 0; box-sizing: border-box; }
  html, body {
    width: 1200px; height: 1200px; overflow: hidden;
    background: var(--backdrop);
    font-family: "Ubuntu", sans-serif;
    color: var(--white);
  }
  .canvas { position: relative; width: 1200px; height: 1200px; }
  .card {
    position: absolute; left: 178px; width: 866px;
    border-radius: 22px; overflow: hidden;
    background: linear-gradient(160deg, var(--card-top), var(--card-bottom));
  }
  .card--front { top: 92px; height: 498px; }
  .card--back { top: 614px; height: 496px; }

  .card__band {
    position: absolute; left: 0; right: 0; bottom: 0; height: 25px;
    background: linear-gradient(90deg, var(--lime), var(--lime-deep));
  }
  .card__rule {
    position: absolute; left: 0; right: 0; height: 3px; background: var(--lime);
  }
  .card--front .card__rule { bottom: 35px; }

  .brand-disc {
    position: absolute; border-radius: 50%;
    background: radial-gradient(circle at 40% 35%, var(--lime), var(--lime-deep));
  }
  .card--front .brand-disc { left: 88px; top: 136px; width: 200px; height: 200px; }
  .brand-name {
    position: absolute; font-weight: 700; color: var(--white); line-height: 1.05;
  }
  .card--front .brand-name { left: 312px; top: 178px; font-size: 58px; }

  .card--back .brand-name { left: 42px; top: 52px; font-size: 36px; }
  .card--back .card__rule { top: 294px; }
  .card--back .brand-disc {
    left: 530px; top: 172px; width: 250px; height: 250px;
    border: 6px solid var(--ink); box-shadow: 0 0 0 4px var(--lime);
  }

  .person { position: absolute; left: 44px; top: 232px; display: flex; gap: 12px; }
  .person__marker { width: 16px; height: 46px; border-radius: 8px; background: var(--lime); margin-top: 4px; }
  .person__name { font-size: 30px; font-weight: 500; line-height: 1.1; }
  .person__role { font-size: 22px; font-weight: 400; margin-top: 2px; }

  .contacts { position: absolute; left: 40px; top: 320px; list-style: none; }
  .contacts__item {
    display: flex; align-items: center; gap: 10px;
    font-size: 18px; height: 24px; margin-bottom: 25px;
  }
  .contacts__item svg { width: 22px; height: 22px; flex: none; }
  .contacts__item--plain { padding-left: 32px; }
</style>
</head>
<body>
<main class="canvas">

  <section class="card card--front" aria-label="Card front">
    <div class="brand-disc" aria-hidden="true"></div>
    <h1 class="brand-name">Pinecrest<br>Premier Motors</h1>
    <div class="card__rule"></div>
    <div class="card__band"></div>
  </section>

  <section class="card card--back" aria-label="Card back">
    <h2 class="brand-name">Pinecrest Premier Motors</h2>

    <div class="person">
      <span class="person__marker"></span>
      <div>
        <p class="person__name">Marcus T Holloran</p>
        <p class="person__role">Owner</p>
      </div>
    </div>

    <div class="card__rule"></div>
    <div class="brand-disc" aria-hidden="true"></div>

    <ul class="contacts">
      <li class="contacts__item">
        <svg viewBox="0 0 24 24" aria-hidden="true"><path fill="#a6c812" d="M6.6 2.5l3 .4 1.2 4.6-2.2 1.6c.9 2.4 2.7 4.6 4.9 6l1.9-2 4.4 1.5.2 3.1c-.1 1-1 1.8-2 1.8C10 19.3 4.6 13.6 4.6 5.5c0-1.6.8-3 2-3z"/></svg>
        <span>(555) 014-3862</span>
      </li>
      <li class="contacts__item">
        <svg viewBox="0 0 24 24" aria-hidden="true"><rect x="2.5" y="5" width="19" height="14" rx="1.5" fill="none" stroke="#a6c812" stroke-width="2"/><path d="M3 6l9 7 9-7M3 18l7-6M21 18l-7-6" fill="none" stroke="#a6c812" stroke-width="1.8"/></svg>
        <span>pineprem@mailvista.example</span>
      </li>
      <li class="contacts__item contacts__item--plain">
        <span>Dealer Lic # 48265</span>
      </li>
    </ul>

    <div class="card__band"></div>
  </section>

</main>
</body>
</html>
```